Verdant Loop Advisors, LLC

I am looking for a simple, clear layout with my logo prominent and embossed, on the best quality card stock available. I would like the business name and phone number included on the card as well......I dont want my name anywhere on the card and I would like my logo embossed on the card......something simple with a white back......open to designs as long as they go along with recycling symbols and green type stuff.....The address, website, cell number, fax number, and email are listed below

5374 Tillbury Fenwood Road
Larkmoor Glen, MD 20699

c. 240.555.0143 f. 240.555.0187
e. sales@verdantloopadvisors.example
w. www.verdantloopadvisors.example

Industry/Entity Type

Recycling

```html
<!DOCTYPE html>
<html lang="en">
<head>
<meta charset="utf-8">
<title>Verdant Loop Advisors, LLC — Business Card</title>
<link href="https://fonts.googleapis.com/css2?family=Arimo:wght@700&display=swap" rel="stylesheet">
<style>
  :root {
    --backdrop: #3a3c3a;
    --card-black: #111211;
    --kraft-light: #dcb88e;
    --kraft-mid: #cfa578;
    --kraft-dark: #c3966a;
    --ink: #1b1a18;
    --leaf-green: #2f9a2c;
    --mark-green: #2d6b25;
  }
  * { box-sizing: border-box; margin: 0; padding: 0; }
  html, body {
    width: 1200px;
    height: 959px;
    overflow: hidden;
    background: var(--backdrop);
  }
  body {
    display: flex;
    align-items: center;
    justify-content: center;
    font-family: "Arimo", Arial, sans-serif;
    font-weight: 700;
    color: var(--ink);
  }
  .business-card {
    position: relative;
    width: 900px;
    height: 540px;
    background: var(--card-black);
    border-radius: 44px;
    box-shadow: 0 18px 40px rgba(0,0,0,0.45);
  }
  .kraft-panel {
    position: absolute;
    left: 34px;
    top: 34px;
    right: 34px;
    bottom: 104px;
    border-radius: 34px 120px 120px 34px;
    background: radial-gradient(ellipse at 35% 40%, var(--kraft-light), var(--kraft-mid) 60%, var(--kraft-dark));
    padding: 46px 60px 0 64px;
  }
  .brand {
    display: flex;
    align-items: center;
    gap: 22px;
  }
  .brand-square {
    width: 62px;
    height: 62px;
    background: var(--mark-green);
    flex: none;
  }
  .brand-name {
    font-size: 44px;
    line-height: 1;
    letter-spacing: 0.5px;
    color: var(--ink);
  }
  .address {
    margin-top: 44px;
    text-align: center;
    font-size: 30px;
    line-height: 1.3;
    padding-left: 60px;
  }
  .contact {
    margin-top: 22px;
    font-size: 29px;
    line-height: 1.35;
  }
  .website {
    position: absolute;
    left: 0;
    right: 0;
    bottom: 36px;
    text-align: center;
    font-size: 30px;
    color: var(--leaf-green);
    letter-spacing: 0.3px;
  }
</style>
</head>
<body>
  <article class="business-card">
    <section class="kraft-panel">
      <div class="brand">
        <span class="brand-square" aria-hidden="true"></span>
        <span class="brand-name">Verdant Loop Advisors, LLC</span>
      </div>
      <p class="address">5374 Tillbury Fenwood Road<br>Larkmoor Glen, MD 20699</p>
      <p class="contact">c. 240.555.0143 &nbsp;f. 240.555.0187<br>e. sales@verdantloopadvisors.example</p>
    </section>
    <p class="website">www.verdantloopadvisors.example</p>
  </article>
</body>
</html>
```